Chia Seed Standup Pouch package design

We are looking for a clean and beautiful standup packaging design for our Organic Chia Seeds.

The package should have a healthy, natural, clean feel to it.

Please see attached Chia Seeds Packaging Samples for further instructions.

***** Requirements *****
- We want two bag style but one design. One will be with a spout and one without a spout.

- Print ready with bleed lines

Reason: We are extending the contest to allow for designers to perfect their designs. Some designs are coming real close to what we would be happy with. Price is now guaranteed. Thank you all for your designs.

Target Market(s)

Health and weight conscious individuals. Our target market are looking for whole natural foods.

Requirements
Must have
• - Include KBRE Organic logo (at minimum, can also include gluten free, vegan, etc)

On the back side of the package:
- have a place that promote our Chia Tea products. For example: "Also try our Sunny Morning Sage Brew, made with Premium organic chia seeds and natural fruits and herbs extracts. (Chia Tea images attached)
Nice to have
• product highlights such as fiber, omega 3, protein, antioxidants, etc.

```html
<!DOCTYPE html>
<html lang="en">
<head>
<meta charset="utf-8">
<title>Verdan Nutrition – Organic Chia Seeds Pouch</title>
<link rel="stylesheet" href="https://fonts.googleapis.com/css2?family=Barlow:wght@500;600;700&family=Barlow+Semi+Condensed:wght@600&display=swap">
<style>
  :root {
    --bg: #ffffff;
    --seal: #e3e4e6;
    --seal-edge: #cfd1d4;
    --paper: #ffffff;
    --green: #8cc63f;
    --green-light: #a9d654;
    --green-deep: #76b12e;
    --yellow: #f6c81e;
    --yellow-pill: #fcd530;
    --pill-text: #5b4a0e;
    --white: #ffffff;
    --seed-dark: #55585c;
    --seed-light: #b9bcc0;
  }
  * { box-sizing: border-box; margin: 0; padding: 0; }
  html, body {
    width: 1200px; height: 675px; overflow: hidden;
    background: var(--bg);
    font-family: "Barlow", sans-serif;
  }
  .lineup {
    position: relative; width: 1200px; height: 675px;
    display: flex; justify-content: center; align-items: center; gap: 45px;
  }
  .pouch {
    position: relative; width: 340px; height: 535px;
    background: var(--seal);
    border: 1px solid var(--seal-edge);
    padding: 12px 12px 8px;
  }
  .pouch-face {
    position: relative; width: 100%; height: 100%;
    overflow: hidden; display: flex; flex-direction: column;
  }
  .brand-band {
    height: 140px; background: var(--paper);
    display: flex; align-items: center; justify-content: center; gap: 10px;
  }
  .brand-dot {
    width: 48px; height: 48px; border-radius: 50%;
    border: 4px solid var(--yellow);
  }
  .brand-name {
    color: var(--yellow); font-weight: 600; font-size: 26px;
    line-height: 0.95; text-transform: uppercase;
  }
  .brand-name span { display: block; font-size: 19px; }
  .product-panel {
    flex: 1; position: relative; text-align: center; color: var(--white);
    background:
      radial-gradient(circle at 85% 12%, rgba(255,255,255,0.22) 0 14%, transparent 30%),
      radial-gradient(circle at 12% 70%, rgba(255,255,255,0.18) 0 12%, transparent 28%),
      radial-gradient(circle at 88% 78%, rgba(255,255,255,0.16) 0 10%, transparent 24%),
      linear-gradient(180deg, var(--green-light), var(--green) 45%, var(--green-deep));
    padding-top: 28px;
  }
  .claim { font-weight: 700; font-size: 15px; }
  .product-name {
    font-family: "Barlow Semi Condensed", sans-serif;
    font-weight: 600; font-size: 50px; line-height: 1; margin-top: 2px;
  }
  .tagline {
    display: inline-block; margin-top: 8px; padding: 3px 18px;
    background: var(--yellow-pill); color: var(--pill-text);
    border-radius: 16px; font-weight: 600; font-size: 17px;
  }
  .highlights { margin-top: 10px; font-weight: 600; font-size: 14.5px; }
  .seed-window {
    width: 124px; height: 124px; margin: 14px auto 0; border-radius: 50%;
    border: 7px solid var(--yellow);
    background: radial-gradient(circle at 40% 35%, var(--seed-light), var(--seed-dark));
  }
  .badges {
    position: absolute; left: 8px; right: 8px; bottom: 10px;
    display: flex; justify-content: center; gap: 9px;
    list-style: none;
  }
  .badge { min-width: 26px; text-align: center; }
  .badge-mark {
    width: 18px; height: 18px; margin: 0 auto; border-radius: 50%;
    border: 1.5px solid var(--white);
  }
  .badge-mark.square { border-radius: 3px; }
  .badge svg { display: block; margin: 0 auto; }
  .badge-label {
    margin-top: 3px; font-size: 5.5px; font-weight: 700;
    text-transform: uppercase; white-space: nowrap;
  }
</style>
</head>
<body>
<main class="lineup">
  <section class="pouch">
    <div class="pouch-face">
      <header class="brand-band">
        <div class="brand-dot"></div>
        <div class="brand-name">Verdan<span>Nutrition</span></div>
      </header>
      <div class="product-panel">
        <p class="claim">100% Organic Raw</p>
        <h1 class="product-name">Chia Seeds</h1>
        <p class="tagline">Ancient Aztec Superfood</p>
        <p class="highlights">2.5 g Omega, 30 g Protein, 5 g Fiber</p>
        <div class="seed-window" role="img" aria-label="Close-up photo of raw chia seeds"></div>
        <ul class="badges">
          <li class="badge"><div class="badge-mark"></div><p class="badge-label">KBRE Certified</p></li>
          <li class="badge"><div class="badge-mark square"></div><p class="badge-label">Vegetarian</p></li>
          <li class="badge"><div class="badge-mark"></div><p class="badge-label">GMO Free</p></li>
          <li class="badge"><div class="badge-mark"></div><p class="badge-label">Gluten Free</p></li>
          <li class="badge"><svg width="18" height="18" viewBox="0 0 18 18"><path d="M3 4 L9 15 L15 3" fill="none" stroke="#fff" stroke-width="2"/></svg><p class="badge-label">Vegan</p></li>
          <li class="badge"><div class="badge-mark"></div><p class="badge-label">Nothing Artificial</p></li>
        </ul>
      </div>
    </div>
  </section>

  <section class="pouch">
    <div class="pouch-face">
      <header class="brand-band">
        <div class="brand-dot"></div>
        <div class="brand-name">Verdan<span>Nutrition</span></div>
      </header>
      <div class="product-panel">
        <p class="claim">100% Organic Raw</p>
        <h1 class="product-name">Chia Seeds</h1>
        <p class="tagline">Ancient Aztec Superfood</p>
        <p class="highlights">2.5 g Omega, 30 g Protein, 5 g Fiber</p>
        <div class="seed-window" role="img" aria-label="Close-up photo of raw chia seeds"></div>
        <ul class="badges">
          <li class="badge"><div class="badge-mark"></div><p class="badge-label">KBRE Certified</p></li>
          <li class="badge"><div class="badge-mark square"></div><p class="badge-label">Vegetarian</p></li>
          <li class="badge"><div class="badge-mark"></div><p class="badge-label">GMO Free</p></li>
          <li class="badge"><div class="badge-mark"></div><p class="badge-label">Gluten Free</p></li>
          <li class="badge"><svg width="18" height="18" viewBox="0 0 18 18"><path d="M3 4 L9 15 L15 3" fill="none" stroke="#fff" stroke-width="2"/></svg><p class="badge-label">Vegan</p></li>
          <li class="badge"><div class="badge-mark"></div><p class="badge-label">Nothing Artificial</p></li>
        </ul>
      </div>
    </div>
  </section>

  <section class="pouch">
    <div class="pouch-face">
      <header class="brand-band">
        <div class="brand-dot"></div>
        <div class="brand-name">Verdan<span>Nutrition</span></div>
      </header>
      <div class="product-panel">
        <p class="claim">100% Organic Raw</p>
        <h1 class="product-name">Chia Seeds</h1>
        <p class="tagline">Ancient Aztec Superfood</p>
        <p class="highlights">2.5 g Omega, 30 g Protein, 5 g Fiber</p>
        <div class="seed-window" role="img" aria-label="Close-up photo of raw chia seeds"></div>
        <ul class="badges">
          <li class="badge"><div class="badge-mark"></div><p class="badge-label">KBRE Certified</p></li>
          <li class="badge"><div class="badge-mark square"></div><p class="badge-label">Vegetarian</p></li>
          <li class="badge"><div class="badge-mark"></div><p class="badge-label">GMO Free</p></li>
          <li class="badge"><div class="badge-mark"></div><p class="badge-label">Gluten Free</p></li>
          <li class="badge"><svg width="18" height="18" viewBox="0 0 18 18"><path d="M3 4 L9 15 L15 3" fill="none" stroke="#fff" stroke-width="2"/></svg><p class="badge-label">Vegan</p></li>
          <li class="badge"><div class="badge-mark"></div><p class="badge-label">Nothing Artificial</p></li>
        </ul>
      </div>
    </div>
  </section>
</main>
</body>
</html>
```